New Website for novelty yarn producer

We need a new website for our company, Tarvek. We make highly tailored yarns for weavers worldwide. This year marks our 40th anniversary and we want to evolve our image and identity.

Our temporary website can be found at:
www.tarvekyarns.com

Our only concern in that throughout the website the protagonist must be our client, we make their creations possible and are highly adaptable both during the ideation process of the yarn as well as in the production. This is at the core of the way we do business and is summarised within the concept of FPM (Fluid Partner Method).

Industry/Entity Type

Textile

Number of Pages Required

1 page

Colors
9bcb3c

Requirements
Must have
• Fluid Partner Method (FPM) - can be found on or current website www.tarvekyarns.com

```html
<!DOCTYPE html>
<html lang="en">
<head>
<meta charset="utf-8">
<title>Tarvek – Novelty Yarns</title>
<link rel="stylesheet" href="https://fonts.googleapis.com/css2?family=Lato:wght@400;700&display=swap">
<style>
  :root{
    --green:#2f7a12;
    --green-line:#6fbf4a;
    --green-band:rgba(98,170,70,.92);
    --ink:#444;
    --body:#5a5a5a;
    --soft:#f6f6f6;
    --footer:#f0f3f7;
    --card-border:#e2e2e2;
  }
  *{box-sizing:border-box;margin:0;padding:0}
  html,body{width:1018px;height:1200px;overflow:hidden}
  body{font-family:"Lato",sans-serif;color:var(--ink);background:#fff;position:relative}
  .section-title{position:absolute;left:0;width:1018px;text-align:center;font-size:27px;font-weight:400;color:var(--ink)}
  .title-rule{position:absolute;height:1px;width:93px;background:var(--green-line)}

  .advantages{position:absolute;left:0;top:0;width:1018px;height:477px;background:var(--soft)}
  .card{position:absolute;top:163px;width:253px;height:231px;background:#fff;border:1px solid var(--card-border);text-align:center}
  .card svg{position:absolute;left:107px;top:36px}
  .card h3{position:absolute;top:86px;left:0;width:100%;font-size:16.5px;font-weight:400;color:var(--green)}
  .card p{position:absolute;top:112px;left:16px;right:16px;font-size:11.6px;line-height:18px;color:var(--body)}

  .news{position:absolute;left:0;top:477px;width:1018px;height:536px;background:#fff}
  .news-item{position:absolute;overflow:hidden}
  .news-item .photo{position:absolute;inset:0}
  .news-item .caption{position:absolute;left:8px;right:10px;bottom:10px;color:#fff;font-size:11.6px;font-weight:700;line-height:18px}
  .news-feature .band{position:absolute;left:0;right:0;bottom:0;height:61px;background:var(--green-band);padding:6px 40px 0 19px;color:#fff;font-size:16.5px;line-height:22px}

  .site-footer{position:absolute;left:0;top:1013px;width:1018px;height:187px;background:var(--footer)}
  .brand{position:absolute;left:114px;top:44px;font-size:21px;font-weight:400;color:#222;letter-spacing:.5px}
  .about{position:absolute;left:114px;top:78px;width:320px;font-size:10.4px;line-height:16.5px;color:var(--body)}
  .company{position:absolute;left:517px;top:41px;font-size:10.2px;line-height:16.5px;color:var(--body)}
  .company strong{color:#333;font-weight:700}
</style>
</head>
<body>

<section class="advantages">
  <h2 class="section-title" style="top:74px">Our Advantages</h2>
  <div class="title-rule" style="left:467px;top:110px"></div>

  <article class="card" style="left:114px">
    <svg width="40" height="40" viewBox="0 0 40 40" fill="none" stroke="var(--green)" stroke-width="1.6" aria-hidden="true">
      <circle cx="26" cy="14" r="10"/><circle cx="26" cy="14" r="3"/>
      <path d="M26 4v20M16 14h20M19 7l14 14M33 7L19 21"/>
      <path d="M4 26h32M6 26v10M34 26v10M6 31h28M8 8l4 18M4 12h8"/>
    </svg>
    <h3>Experience</h3>
    <p>Over the years the company has gained the knowledge and skills that define the superiority of our product and the rigor of our work ethic</p>
  </article>

  <article class="card" style="left:382px">
    <svg width="40" height="40" viewBox="0 0 40 40" fill="none" stroke="var(--green)" stroke-width="1.6" aria-hidden="true">
      <path d="M12 24c-5 0-7-4-5-7-3-3 0-8 4-7 1-4 7-5 9-2 2-3 8-2 9 2 4-1 7 4 4 7 2 3 0 7-5 7"/>
      <path d="M20 14v8M16 17c2 2 6 2 8 0M16 24h8v5h-8zM17 32h6M18 35h4"/>
      <path d="M20 2v3M6 6l2 2M34 6l-2 2M3 30l3-1M37 30l-3-1"/>
    </svg>
    <h3>Creativity</h3>
    <p>The key to our clients' success is a combination of innovation, creativity and quality. We implement these principles in order to meet and exceed our clients' demands (every time)</p>
  </article>

  <article class="card" style="left:651px">
    <svg width="40" height="40" viewBox="0 0 40 40" fill="none" stroke="var(--green)" stroke-width="1.6" aria-hidden="true">
      <path d="M15 2h10v14l-5 4-5-4zM3 8h8v12l-4 4-4-4zM29 8h8v12l-4 4-4-4z"/>
      <circle cx="7" cy="33" r="4"/><circle cx="33" cy="33" r="4"/>
      <path d="M20 24l2 4h4l-3 3 1 4-4-2-4 2 1-4-3-3h4z"/>
      <path d="M7 24v5M33 24v5"/>
    </svg>
    <h3>Professionality</h3>
    <p>We are a family business at the core. Our company is run with the same values as the Ferrante family: respect, determination and commitment.</p>
  </article>
</section>

<section class="news">
  <h2 class="section-title" style="top:76px">Latest News</h2>
  <div class="title-rule" style="left:462px;top:110px"></div>

  <article class="news-item news-feature" style="left:114px;top:163px;width:522px;height:283px">
    <div class="photo" role="img" aria-label="Close-up photo of a chunky cable-knit beige wool fabric" style="background:radial-gradient(ellipse at 50% 55%,#a08a5e 0%,#8a7550 50%,#6e5d40 100%)"></div>
    <div class="band">At vero eos et accusamus et iusto odio dignissi mos ducimus qui blanditiis</div>
  </article>

  <article class="news-item" style="left:651px;top:163px;width:254px;height:134px">
    <div class="photo" role="img" aria-label="Photo of orange and dark knitted garments piled together" style="background:linear-gradient(135deg,#2e2c26 0%,#6a4a2a 40%,#a8673a 65%,#3a302a 100%)"></div>
    <p class="caption">At vero eos et accusamus et iusto odio dig nissi mos ducimus qui blanditiis</p>
  </article>

  <article class="news-item" style="left:651px;top:312px;width:254px;height:134px">
    <div class="photo" role="img" aria-label="Photo of colourful hanging fabrics in teal, yellow, red and mauve" style="background:linear-gradient(90deg,#1f3a3c 0%,#2a5a58 25%,#b59a2a 42%,#8a3a3a 58%,#8a7288 78%,#3a4a50 100%)"></div>
    <p class="caption">At vero eos et accusamus et iusto odio dig nissi mos ducimus qui blanditiis</p>
  </article>
</section>

<footer class="site-footer">
  <div class="brand">Tarvek</div>
  <p class="about">Tarvek combines the experience of a team that has served the weaving industry for over 40 years, fully dedicated to the success of our clients</p>
  <address class="company" style="font-style:normal">
    <strong>Velmar s.r.l</strong><br>
    Via dei Telai 48 - 59012 Borgo Lana - Italy - Tel. 0555 41872 r.a.<br>
    Fax 0555 418790<br>
    R.E.A BL 481293- Reg. Imp. BL 04812930215<br>
    <strong>P. IVA 00482930711</strong> - Cod. Fisc. 04812930215<br>
    Capitale sociale € 84. 260, 00 int. ver.
  </address>
</footer>

</body>
</html>
```